Package Storage Service

Ideas...

Business Name... "TUCK IT AT BRAMWOOD":
Store it,
Don’t Ship it;
4-LESS
Convenience, Quality, Service

Easy as ABC…
A. Contact Us 064-293-5527
B. We deliver
C. We pick-up & Store

LESS, is the new MORE

Box Size* (Approx) Weight Limit Price per Month
41 cm X 34 cm X 26 cm 10 Kilos 12 CHFs/per month
48 cm X 43 cm X 35 cm 25 Kilos 25 CHFs/per month

* Larger sizes and prices available upon request.

Contact: Tom /064-293-5527

These are only ideas for a small package storage service for local college students. The storage times are usually for 1 - 3 months.
I need a catchy, creative, colorful design for a new business.

This flyer will need to be printable in color. A-4 size or 8 1/2 " X 11".

Target Market(s)

Hotel Management students leaving their program for vacations for short terms. They return after vacation or after practical work experiences 4 study.

Industry/Entity Type

College

Requirements
Must have
• Prices, box sizes, catchy format.

Idea will forward to their address should they not return to the school; for a postage fee + 15.00 CHFs.

Contact information for the PICKUP and DELIVERY Service... see above.

Include a PICKUP AND DELIVERY Option in the flyer.
Nice to have
• Colorful boxes with a creative idea for someone to choose spending a little each month rather than a lot at one time. 25 CHFs rather than 125 CHFs.
Should not have
• Not too wordy.

```html
<!DOCTYPE html>
<html lang="en">
<head>
<meta charset="utf-8">
<title>Tuck It at Bramwood – Package Storage</title>
<link rel="stylesheet" href="https://fonts.googleapis.com/css2?family=Arimo:ital,wght@0,400;0,700;1,700&family=Gochi+Hand&display=swap">
<style>
  :root {
    --blue: #1a5ee8;
    --red: #f00a18;
    --green: #0a9418;
    --orange: #fdb940;
    --ink: #111111;
    --white: #ffffff;
    --frame: #1c1c1c;
  }
  * { margin: 0; padding: 0; box-sizing: border-box; }
  html, body { width: 921px; height: 1200px; overflow: hidden; background: var(--white); }
  .flyer {
    position: relative;
    width: 921px;
    height: 1200px;
    font-family: "Arimo", Arial, sans-serif;
    overflow: hidden;
  }
  .dots { position: absolute; left: 0; top: 0; }
  .brand {
    position: absolute;
    top: 4px; left: 0; width: 921px;
    text-align: center;
    color: var(--blue);
    font-weight: 700;
    font-size: 62px;
    letter-spacing: 1px;
  }
  .tagline {
    position: absolute;
    left: 352px; top: 94px;
    color: var(--red);
    font-weight: 700;
    font-size: 44px;
  }
  .values {
    position: absolute;
    left: 354px; top: 166px;
    color: var(--green);
    font-weight: 700;
    font-style: italic;
    font-size: 26px;
  }
  .easy {
    position: absolute;
    left: 34px; top: 200px; width: 282px;
    text-align: center;
    font-family: "Gochi Hand", cursive;
    font-size: 68px;
    line-height: 76px;
    color: var(--ink);
  }
  .steps {
    position: absolute;
    left: 52px; top: 405px; width: 312px;
    text-align: center;
    color: var(--white);
    font-style: italic;
    font-size: 30px;
    line-height: 46px;
  }
  .photo {
    position: absolute;
    border: 8px solid var(--frame);
  }
  .photo-packer {
    left: 431px; top: 265px; width: 423px; height: 328px;
    background: linear-gradient(120deg, #f4f2f0 0%, #e6d2cc 40%, #d84a8c 60%, #c8a47a 85%, #f5f3f0 100%);
  }
  .photo-mover {
    left: 554px; top: 668px; width: 285px; height: 402px;
    background: linear-gradient(180deg, #eeeeee 0%, #d8b685 35%, #c49560 55%, #6f7f96 72%, #b47a44 100%);
  }
  .slogan {
    position: absolute;
    left: 56px; top: 690px;
    color: var(--green);
    font-weight: 700;
    font-size: 62px;
    line-height: 78px;
  }
  .price-head {
    position: absolute;
    left: 59px; top: 876px;
    color: var(--red);
    font-size: 20px;
  }
  .price-row {
    position: absolute;
    left: 32px;
    display: flex;
    align-items: center;
    gap: 20px;
    color: var(--red);
    font-size: 18px;
  }
  .price-row .swatch { width: 36px; height: 36px; border-radius: 50%; }
  .row-small { top: 932px; }
  .row-small .swatch { background: var(--green); }
  .row-large { top: 983px; }
  .row-large .swatch { background: var(--orange); }
  .note {
    position: absolute;
    left: 92px; top: 1040px;
    color: var(--red);
    font-size: 15px;
  }
  .contact-band {
    position: absolute;
    left: 0; top: 1082px; width: 884px; height: 118px;
    background: var(--green);
    color: var(--white);
    font-size: 56px;
    display: flex;
    align-items: center;
    justify-content: center;
  }
</style>
</head>
<body>
<div class="flyer">
  <svg class="dots" width="921" height="1200" viewBox="0 0 921 1200" aria-hidden="true">
    <circle cx="631" cy="304" r="111" fill="var(--blue)"/>
    <circle cx="383" cy="279" r="67" fill="var(--green)"/>
    <circle cx="401" cy="448" r="89" fill="var(--red)"/>
    <circle cx="175" cy="289" r="141" fill="var(--orange)"/>
    <circle cx="208" cy="518" r="156" fill="var(--blue)"/>
    <circle cx="386" cy="607" r="45" fill="var(--green)"/>
    <circle cx="757" cy="716" r="119" fill="var(--blue)"/>
    <circle cx="520" cy="680" r="67" fill="var(--red)"/>
  </svg>

  <h1 class="brand">TUCK IT AT BRAMWOOD</h1>
  <p class="tagline">Store it, Don’t Ship it!</p>
  <p class="values">4-Less Convenience, Quality, Service</p>

  <p class="easy">Easy as<br>ABC</p>

  <p class="steps">Contact Us<br>064-293-5527<br>We Deliver<br>We Pick-up &amp;<br>Store</p>

  <div class="photo photo-packer" role="img" aria-label="Photo of a young woman packing a cardboard storage box"></div>
  <div class="photo photo-mover" role="img" aria-label="Photo of a person carrying a stack of cardboard boxes in a bright room"></div>

  <p class="slogan">LESS, is the<br>New MORE</p>

  <p class="price-head">Box Size* (Approx) Weight Limit Price per Month</p>
  <div class="price-row row-small"><span class="swatch"></span><span>41 cm X 34 cm X 26 cm 10 Kilos 12 CHFs/per month</span></div>
  <div class="price-row row-large"><span class="swatch"></span><span>48 cm X 43 cm X 35 cm 25 Kilos 25 CHFs/per month</span></div>
  <p class="note">*Larger sizes and prices available upon request</p>

  <div class="contact-band">Contact: Tom 064-293-5527</div>
</div>
</body>
</html>
```